Modern Business Card

Modern professional business card with more than just logo and demographic info. Something memorable.

We are a trendy/modern chiropractic group with an emphasis on neurology, hence the minimalist-type brain logo. We want to convey that modern and technical aspect with professionalism and the elite nature of our practice environment.

```html
<!DOCTYPE html>
<html lang="en">
<head>
<meta charset="utf-8">
<title>Cortex Chiropractic – Business Card</title>
<link href="https://fonts.googleapis.com/css2?family=Montserrat:wght@400;500;700&family=Open+Sans:wght@400;600&display=swap" rel="stylesheet">
<style>
  :root {
    --brand-blue: #3f7ac0;
    --ink: #151515;
    --paper: #ffffff;
    --paper-shade: #ececec;
    --backdrop: #e4e4e2;
  }
  * { margin: 0; padding: 0; box-sizing: border-box; }
  html, body { width: 1200px; height: 900px; overflow: hidden; }
  body {
    background: var(--backdrop);
    font-family: "Open Sans", sans-serif;
    color: var(--ink);
    position: relative;
  }
  .card {
    position: absolute;
    left: 320px;
    width: 560px;
    height: 320px;
    border-radius: 14px;
    overflow: hidden;
    background: linear-gradient(160deg, var(--paper) 0%, var(--paper-shade) 100%);
    box-shadow: 0 10px 30px rgba(0,0,0,.18);
  }
  .card--front { top: 90px; }
  .card--back { top: 470px; }

  /* front */
  .front-band {
    position: absolute; left: 0; right: 0; bottom: 0; height: 12px;
    background: var(--brand-blue);
  }
  .front-tab {
    position: absolute; left: 0; top: 150px; width: 10px; height: 34px;
    background: var(--brand-blue);
  }
  .brand-name {
    position: absolute; right: 34px; top: 40px;
    display: flex; align-items: center; gap: 10px;
    font-family: "Montserrat", sans-serif; font-weight: 500;
    font-size: 20px; letter-spacing: 1.5px; color: var(--brand-blue);
    line-height: 1.1;
  }
  .brand-name__mark { width: 14px; height: 14px; background: var(--brand-blue); }
  .divider {
    position: absolute; left: 200px; right: 34px; top: 150px;
    height: 1px; background: var(--ink);
  }
  .person { position: absolute; left: 42px; top: 118px; }
  .person__name {
    font-family: "Montserrat", sans-serif; font-size: 28px;
    letter-spacing: .5px; font-weight: 400; line-height: 1;
  }
  .person__name strong { font-weight: 700; }
  .person__role {
    font-family: "Montserrat", sans-serif; font-size: 14px; margin-top: 5px;
    letter-spacing: .5px;
  }
  .person__rule {
    margin-top: 6px; width: 160px; height: 3px; background: var(--brand-blue);
  }
  .contact { position: absolute; left: 42px; top: 212px; list-style: none; }
  .contact__item {
    display: flex; align-items: center; gap: 16px;
    font-size: 15px; letter-spacing: .8px; margin-bottom: 14px;
  }
  .icon-box {
    width: 26px; height: 22px; border-radius: 3px; background: var(--brand-blue);
    display: flex; align-items: center; justify-content: center;
  }
  .address {
    position: absolute; right: 34px; top: 175px; text-align: right;
    font-size: 15px; font-weight: 600; letter-spacing: .6px; line-height: 1.35;
  }
  .address .icon-box { margin: 0 0 8px auto; }

  /* back */
  .back-art { position: absolute; inset: 0; }
</style>
</head>
<body>

<section class="card card--front" aria-label="Business card front">
  <div class="front-tab"></div>
  <div class="brand-name"><span class="brand-name__mark"></span>CORTEX CHIROPRACTIC</div>
  <div class="divider"></div>

  <div class="person">
    <p class="person__name"><strong>DANIEL</strong> REED</p>
    <p class="person__role">FOUNDER &amp; CEO</p>
    <div class="person__rule"></div>
  </div>

  <ul class="contact">
    <li class="contact__item">
      <span class="icon-box">
        <svg width="10" height="14" viewBox="0 0 10 14"><rect x="1" y="1" width="8" height="12" rx="1.5" fill="none" stroke="#fff" stroke-width="1.5"/></svg>
      </span>
      012-345-6789
    </li>
    <li class="contact__item">
      <span class="icon-box">
        <svg width="14" height="12" viewBox="0 0 14 12"><circle cx="2" cy="10" r="1.5" fill="#fff"/><path d="M1 5a6 6 0 0 1 6 6M1 1a10 10 0 0 1 10 10" fill="none" stroke="#fff" stroke-width="1.5"/></svg>
      </span>
      www.domainname.com
    </li>
  </ul>

  <div class="address">
    <span class="icon-box">
      <svg width="10" height="14" viewBox="0 0 10 14"><path d="M5 13C2 9 1 7 1 5a4 4 0 0 1 8 0c0 2-1 4-4 8z" fill="#fff"/><circle cx="5" cy="5" r="1.5" fill="#3f7ac0"/></svg>
    </span>
    Address, Suit, Floor<br>City, Country, Zipcode
  </div>
  <div class="front-band"></div>
</section>

<section class="card card--back" aria-label="Business card back">
  <svg class="back-art" width="560" height="320" viewBox="0 0 560 320">
    <polygon points="0,130 217,0 500,0 0,300" fill="var(--brand-blue)"/>
    <line x1="430" y1="0" x2="560" y2="-78" stroke="var(--brand-blue)"/>
    <line x1="470" y1="36" x2="560" y2="-18" stroke="var(--brand-blue)" stroke-width="1"/>
    <line x1="180" y1="320" x2="300" y2="248" stroke="var(--brand-blue)" stroke-width="1"/>
    <line x1="440" y1="164" x2="560" y2="92" stroke="var(--brand-blue)" stroke-width="1"/>
    <g transform="translate(150,200) rotate(-31)">
      <rect x="0" y="-16" width="18" height="18" fill="#fff"/>
      <text x="30" y="0" font-family="Montserrat, sans-serif" font-weight="500" font-size="24" letter-spacing="2" fill="#fff">CORTEX CHIROPRACTIC</text>
    </g>
    <text transform="translate(308,252) rotate(-31)" font-family="Open Sans, sans-serif" font-size="15" letter-spacing="1" fill="var(--brand-blue)">www.domainname.com</text>
  </svg>
</section>

</body>
</html>
```